New Menu for Elegant Cafe Pastry Shop

We need to choose a design and layout for our new menu. We would like to also condense our current menu to 4-6 pages.
We will be changing prices and items on the menu, so it needs to be editable. Adobe formats are preferred. The size of the pages needs to be letter size. We will be printing it in house
Please take inspiration from the photos of our shop and food and also our Picmosaic page.
Attached are our current menu our logo and the logo info

https://www.picmosaic.com/marbrecoquette/?hl=en
https://maps.wayfindr.app/Qk3Lm9Xp2Tb7VwR4a

Industry/Entity Type

Food Cafe Bakery pastry

Other font styles liked:
• please look at attached files

Colors

Designer to choose colors to be used in the design.

Requirements
Nice to have
• Use of Arches like on our shop wallpaper or oblong eclair shapes, Art Deco elements

```html
<!DOCTYPE html>
<html lang="en">
<head>
<meta charset="utf-8">
<title>Marbre Coquette — Menu</title>
<link href="https://fonts.googleapis.com/css2?family=Poiret+One&family=Cormorant+Garamond:wght@500;600&family=Montserrat:wght@400&display=swap" rel="stylesheet">
<style>
:root{
  --teal:#4db7c5;
  --ink:#2e2424;
  --frame:#7a6a6a;
  --rule:#c9c2c2;
  --cover:#ececec;
  --paper:#ffffff;
}
*{box-sizing:border-box;margin:0;padding:0}
html,body{width:849px;height:1200px;overflow:hidden;background:var(--paper)}
body{position:relative;font-family:"Cormorant Garamond",serif;color:var(--ink)}
.spread{position:absolute;left:146px;width:556px;height:359px;background:var(--paper);border:1px solid #444;box-shadow:3px 5px 7px rgba(0,0,0,.18)}
.spread-1{top:32px}.spread-2{top:421px}.spread-3{top:809px}
.page{position:absolute;top:0;width:278px;height:357px}
.page-left{left:0}
.page-right{left:278px}
.page-split{border-right:1px solid #444}
.page-title{position:absolute;top:8px;left:0;right:0;text-align:center;font-family:"Poiret One",sans-serif;color:var(--teal);font-size:17px;line-height:1}
.page-kicker{position:absolute;top:28px;left:0;right:0;text-align:center;font-size:5px;letter-spacing:.3px}
.frame{position:absolute;left:8px;right:8px;top:38px;bottom:13px;border:2px double var(--frame);padding:5px 6px;display:flex;flex-direction:column}
.legend{position:absolute;bottom:3px;left:0;right:0;text-align:center;font-size:2.8px;letter-spacing:.1px}
.sec{font-family:"Poiret One",sans-serif;color:var(--teal);font-size:12px;line-height:1;text-align:center}
.sec-lg{font-size:15px}
.note{font-size:3.6px;text-align:center;text-transform:uppercase}
.cols2,.cols3{display:grid}
.cols2{grid-template-columns:1fr 1fr}
.cols3{grid-template-columns:1fr 1fr 1fr}
.cols2>div+div,.cols3>div+div{border-left:1px solid var(--rule)}
.cols2>div,.cols3>div{padding:0 3px}
.hr{border-top:1px solid var(--rule);margin:4px 4px}
.item{text-align:center;margin-top:5px}
.name{font-size:4.8px;font-weight:500;text-transform:uppercase;line-height:1.2}
.gf{font-size:3.4px;font-family:Montserrat,sans-serif}
.desc{font-family:Montserrat,sans-serif;font-size:3.3px;line-height:1.25;margin:1px 4px 0}
.price{color:var(--teal);font-size:4.8px}
.list{text-align:center;font-size:4.6px;line-height:8px;text-transform:uppercase;margin-top:2px}
.list .price{font-size:4.6px}
.box{border:1px solid var(--frame);outline:1px solid var(--frame);outline-offset:1px}
.table{width:100%;font-size:4px;text-transform:uppercase;border-collapse:collapse}
.table td{padding:1.5px 0}
.table td:last-child{text-align:right;color:var(--teal)}
.cover{background:var(--cover)}
.cover-art{position:absolute;left:24px;top:30px;width:230px;height:300px;border-radius:115px 115px 30px 30px;background:radial-gradient(ellipse at 50% 55%,#ddd6d6 0%,#e6e2e2 45%,var(--cover) 75%)}
.cover-name{position:absolute;left:0;right:0;top:206px;text-align:center;font-size:15px;font-weight:600;letter-spacing:1px;color:var(--ink)}
.cover-label{position:absolute;left:0;right:0;top:255px;text-align:center;font-size:5px;letter-spacing:1px}
.cover-url{position:absolute;left:0;right:0;top:316px;text-align:center;font-size:5px;letter-spacing:1px}
.grow{flex:1}
</style>
</head>
<body>

<!-- Spread 1 -->
<section class="spread spread-1">
  <div class="page page-left page-split">
    <h1 class="page-title">Sweet Eclairs</h1>
    <div class="frame">
      <div class="cols2 grow">
        <div>
          <div class="sec">Single</div>
          <div class="item" style="margin-top:0"><div class="name">Chocolatee Clair</div><div class="gf">(GF available)</div><div class="desc">The classic chocolate: pastry filling with chocolate glaze</div><div class="price">$5.20</div></div>
          <div class="item"><div class="name">Vanilla Éclair</div><div class="gf">(GF available)</div><div class="desc">The classic: vanilla pastry filling with chocolate glaze</div><div class="price">$5.50</div></div>
          <div class="item"><div class="name">Coffee Éclair</div><div class="desc">Coffee creamy filling with a Caramel Coffee Glaze</div><div class="price">$6.55</div></div>
          <div class="item"><div class="name">Tresleches Éclair</div><div class="gf">(GF available)</div><div class="desc">Tres leches cream perfumed with real rum and cinnamon, glaze in white chocolate</div><div class="price">$6.55</div></div>
          <div class="item"><div class="name">Guava Éclair</div><div class="gf">(GF available)</div><div class="desc">The guava pastry filling with pink sweet glaze</div><div class="price">$6.55</div></div>
          <div class="item"><div class="name">Strawberry Éclair</div><div class="desc">The vanilla pastry cream and strawberry jam, dipped in red glaze</div><div class="price">$6.55</div></div>
          <div class="item"><div class="name">Creme Brulee Éclair</div><div class="desc">The filled with classic vanilla pastry cream and dipped in hard caramel</div><div class="price">$6.55</div></div>
        </div>
        <div>
          <div class="sec">Double</div>
          <div class="item" style="margin-top:0"><div class="name">German Chocolate Éclair (CN)</div><div class="desc">Chocolate cream filling topped with a rich sticky coconut and pecan paste dipped in hard dark chocolate with touches of gold</div><div class="price">$5.70</div></div>
          <div class="item"><div class="name">Tiramisu Éclair</div><div class="desc">Double éclair filled with vanilla custard cream flavored with espresso coffee cream and topped with a rich mascarpone cream with an insert of lady fingers cake</div><div class="price">$5.70</div></div>
          <div class="item"><div class="name">Baklava Éclair (CN)</div><div class="desc">Filled with orange pastry cream, decorated with caramelized pistachios and pieces of fyllo dough drizzled with honey and cinnamon</div><div class="price">$5.70</div></div>
          <div class="item"><div class="name">Tropical Passion Éclair</div><div class="desc">Double eclair filled with mango pastry cream topped with light passion fruit panna cotta with an insert of mango gelée</div><div class="price">$6.55</div></div>
          <div class="item"><div class="name">Macarons</div><div class="gf">(Contain Almonds)</div><div class="desc">White Chocolate | Dark Chocolate | Lemon | Apricot | Raspberry | Pistachio (contains pistachio and almond)</div><div class="price">$3.20</div></div>
          <div class="box" style="margin-top:4px;padding:2px 3px">
            <div class="sec" style="font-size:11px">Bread Puddings (CN)</div>
            <table class="table"><tr><td>Mango &amp; White Chocolate (CA)</td><td>$5.20</td></tr><tr><td>Guava (CA)</td><td>$5.20</td></tr><tr><td>Brownie Walnut (contains walnuts)</td><td>$5.20</td></tr><tr><td>Add a scoop of vanilla ice-cream</td><td>+$2.50</td></tr></table>
          </div>
        </div>
      </div>
      <div class="hr" style="margin:4px 24px"></div>
      <div class="cols2 box" style="margin:2px 46px 6px">
        <div class="item" style="margin:1px 0"><div class="sec">Cake Pops</div><div class="desc">Vanilla | Chocolate | Carrot Cake | V G.f. Brownie (contains chickpeas) $3.50</div></div>
        <div class="item" style="margin:1px 0"><div class="sec">Meringues</div><div class="desc">Meringue box $3.70</div></div>
      </div>
    </div>
    <div class="legend">(CN) - CONTAINS NUTS (CA) - CONTAINS ALMONDS (CW) - CONTAINS WALNUTS (GF) - GLUTEN FREE (V) - VEGAN</div>
  </div>
  <div class="page page-right cover">
    <div class="cover-art" role="img" aria-label="Arched line-art frame with scrollwork around the cafe emblem"></div>
    <div class="cover-name">MARBRE COQUETTE</div>
    <div class="cover-label">MENU</div>
    <div class="cover-url">WWW.MARBRECOQUETTE.COM</div>
  </div>
</section>

<!-- Spread 2 -->
<section class="spread spread-2">
  <div class="page page-left">
    <h1 class="page-title">Mocktails</h1>
    <div class="frame">
      <div class="cols3">
        <div class="item" style="margin:0"><div class="sec">Pina Colada</div><div class="name" style="margin-top:2px">A tropical classic mocktail of pineapple and coconut</div><div class="price">$ 6.30</div></div>
        <div class="item" style="margin:0"><div class="sec">Mango Lychee</div><div class="name" style="margin-top:2px">Refreshing mix of lychee and mango</div><div class="price">$ 6.50</div></div>
        <div class="item" style="margin:0"><div class="sec">Ruby Temple</div><div class="name" style="margin-top:2px">Ginger ale and grenadine mocktail garnished with maraschino cherry.</div><div class="price">$ 6.30</div></div>
      </div>
      <div class="hr"></div>
      <div class="sec sec-lg">Coffees &amp; Beverages</div>
      <div class="cols3" style="margin-top:3px">
        <div><div class="sec">Iced Coffee</div><div class="list">Iced Espresso <span class="price">$4.00</span><br>Iced Cappuccino <span class="price">$4.55</span><br>Iced Latte <span class="price">$4.75</span></div></div>
        <div><div class="sec">Hot Coffee</div><div class="list">Filter Coffee <span class="price">$2.40</span><br>Espresso <span class="price">$2.75</span><br>Cappuccino <span class="price">$3.50</span><br>Latte <span class="price">$3.70</span><br>Americano <span class="price">$3.00</span><br>Espresso Macchiato <span class="price">$3.00</span></div></div>
        <div><div class="sec">Matcha</div><div class="list">Matcha Tea <span class="price">$3.20</span><br>Matcha Latte Hot <span class="price">$3.95</span><br>Matcha Latte Cold <span class="price">$3.95</span></div></div>
      </div>
      <div class="hr"></div>
      <div class="sec sec-lg">Syrups - Sauces - Toppings</div>
      <div class="list" style="line-height:6px;margin-top:4px;font-size:4px">Vanilla | Hazelnut | Caramel | Mocha | Lavender | Almond (ask for our sugar free options) +$1.00<br>Dark or White Chocolate Sauce +$1.00 Extra Shot +$1.00 Decaf +$1.00</div>
      <div class="hr"></div>
      <div class="cols3 grow">
        <div><div class="sec">Cold Drinks</div><div class="list">Isla Water 16 oz <span class="price">$3.70</span><br>San Pietrino <span class="price">$4.70</span><br>Cola Classica / Diet <span class="price">$4.00</span><br>Perlier <span class="price">$4.70</span><br><br>Homemade Lemonade <span class="price">$6.50</span><br>Mint Lemonade <span class="price">$6.50</span><br>Strawberry Lemonade <span class="price">$6.50</span><br>Lavender Lemonade <span class="price">$6.50</span><br>Orange Juice <span class="price">$4.70</span></div></div>
        <div><div class="sec">Tea</div><div class="list">Earl Grey <span class="price">$3.50</span><br>Darjeeling <span class="price">$3.50</span><br>Ginger Lemongrass <span class="price">$3.50</span><br>Camomile <span class="price">$3.50</span><br>Mint Vervain &amp; Herbs <span class="price">$3.50</span><br>Fruit Symphony <span class="price">$3.50</span><br>Dragon Sencha Green Tea <span class="price">$3.50</span><br>Iced Tea <span class="price">$3.50</span></div></div>
        <div><div class="sec">Chocolate</div><div class="list">Chocolate Hot <span class="price">$4.95</span><br>Chocolate Cold <span class="price">$4.95</span><br>Whipped Cream <span class="price">+$1.00</span></div></div>
      </div>
    </div>
    <div class="legend">(CN) - CONTAINS NUTS (CA) - CONTAINS ALMONDS (CW) - CONTAINS WALNUTS (GF) - GLUTEN FREE (V) - VEGAN</div>
  </div>
  <div class="page page-right">
    <h1 class="page-title">All Day Brunch</h1>
    <div class="page-kicker">UNIQUE FLAVORS</div>
    <div class="frame">
      <div class="cols3">
        <div class="item" style="margin:0"><div class="sec">Grilled cheese sandwich</div><div class="desc">Big chou bun 2 slices of fontina cheese, ham and bacon* ~ the ultimate grilled cheese sandwich "a la eclair"</div><div class="price">$14.00</div></div>
        <div class="item" style="margin:0"><div class="sec">Croque Monsieur</div><div class="desc">Big chou bun served hot filled with creamy bechamel sauce, gruyère cheese, ham and bacon*</div><div class="price">$15.00</div></div>
        <div class="item" style="margin:0"><div class="sec">Croque Madame</div><div class="desc">Big chou bun served hot filled with creamy bechamel sauce, gruyère cheese, ham and bacon* and topped with an egg sunny side up</div><div class="price">$16.50</div></div>
      </div>
      <div class="hr"></div>
      <div class="cols2">
        <div>
          <div class="sec">Eggcellent Choices</div><div class="note">Also available: gluten free bun</div>
          <div class="item"><div class="name">Eggs Florentine</div><div class="desc">Chou bun topped with chive cream cheese, sauté spinach, 2 eggs and pink hollandaise sauce</div><div class="price">$16.45</div></div>
          <div class="item"><div class="name">Eggs Benedict</div><div class="desc">Chou bun topped whipped chive cream cheese, ham, 2 eggs, and pink hollandaise sauce</div><div class="price">$16.45</div></div>
          <div class="item"><div class="name">Avocado &amp; Eggs</div><div class="desc">Chou bun topped with chunky avocado smash, crumbled feta, 2 eggs, topped with spicy honey, oil, chili flakes and sesame</div><div class="price">$17.45</div></div>
          <div class="item"><div class="name">Eggs Royal</div><div class="desc">Chou bun, topped with whipped cream cheese with chives, smoked salmon, diced red onion, 2 eggs, pink hollandaise sauce, sesame seeds</div><div class="price">$18.50</div></div>
        </div>
        <div>
          <div class="sec">Pancakes</div>
          <div class="item"><div class="name">O.M.G. Eggs $ Bacon</div><div class="desc">4 pancakes topped with grated gruyère, bacon, an egg sunny side up and served with a side of maple syrup</div><div class="price">$16.50</div></div>
          <div class="item"><div class="name">Classic Nocciella &amp; Berries</div><div class="desc">4 pancakes topped with Nocciella, fresh berries and whipped cream</div><div class="price">$16.50</div></div>
          <div class="item"><div class="name">Tropical Guava &amp; Cheese</div><div class="desc">4 pancakes topped with guava cream, cream cheese frosting, fresh raspberries and raspberry syrup</div><div class="price">$16.00</div></div>
          <div class="item"><div class="name">Oriental (CN)</div><div class="desc">4 pancakes topped with Orange cream, caramelized pistachios, crunchy phyllo and drizzled with honey cinnamon syrup</div><div class="price">$14.50</div></div>
        </div>
      </div>
      <div class="hr"></div>
      <div class="sec sec-lg">Sides</div>
      <div class="cols2" style="margin:3px 36px 0">
        <div style="border:none"><table class="table"><tr><td>Eggs(1)</td><td>$2.99</td></tr><tr><td>Bacon (4 slices)</td><td>$4.00</td></tr><tr><td>Salmon</td><td>$3.50</td></tr><tr><td>Pancakes (2)</td><td>$3.50</td></tr></table></div>
        <div style="border:none;padding-left:10px"><table class="table"><tr><td>Avocado Smash</td><td>$2.50</td></tr><tr><td>Fruit Bowl</td><td>$5.25</td></tr><tr><td>Green Salad</td><td>$3.50</td></tr></table></div>
      </div>
      <div class="note" style="font-size:4.4px;margin-top:3px">* Also available: turkey bacon, turkey ham</div>
    </div>
    <div class="legend">(CN) - CONTAINS NUTS (CA) - CONTAINS ALMONDS (CW) - CONTAINS WALNUTS (GF) - GLUTEN FREE (V) - VEGAN</div>
  </div>
</section>

<!-- Spread 3 -->
<section class="spread spread-3">
  <div class="page page-left">
    <h1 class="page-title">Lunch</h1>
    <div class="frame">
      <div class="cols3">
        <div>
          <div class="sec">Salads</div>
          <div class="item" style="margin-top:2px"><div class="name">Greek</div><div class="desc">Baby tomatoes, cucumbers, feta, olives, onions, P.O.V. olive oil, vinegar</div><div class="price">$5.50</div></div>
          <div class="item"><div class="name">Garden Roquefort</div><div class="desc">Baby greens, arugula, beets, Roquefort P.O.V. blue cheese, caramelized pistachios, strawberries, orange vinaigrette</div><div class="price">$5.50</div></div>
          <div class="item"><div class="name">Zucchini</div><div class="desc">Fresh spiralized zucchini with feta, mint, almonds, lemon, POV olive oil</div><div class="price">$6.55</div></div>
        </div>
        <div>
          <div class="sec">Soups</div>
          <div class="item" style="margin-top:2px"><div class="name">French Onion Soup</div><div class="desc">Classic onion soup gratinated with gruyere cheese and crunchy eclairs</div><div class="price">$7.95</div></div>
          <div class="item"><div class="name">Pumpkin Soup</div><div class="desc">Homemade pumpkin soup served with cream and crushed chickpeas</div><div class="price">$6.60</div></div>
          <div class="item"><div class="name">Tomato Soup</div><div class="desc">Tomato soup served with prosciutto gruyere cheese and crunchy eclairs</div><div class="price">$7.60</div></div>
        </div>
        <div>
          <div class="sec">Quiches</div>
          <div class="note" style="margin-top:2px">Available also in GF crust</div>
          <div class="list" style="line-height:7px">• Lorraine<br>• Mushroom<br>• Spinach<br>• Salmon Tomato<br><span class="price">$6.99</span></div>
          <div class="item" style="margin-top:1px"><div class="sec">Phyllo Pocket</div><div class="desc">Feta cheese served hot drizzled with honey and sesame</div><div class="price">$4.60</div></div>
          <div class="item" style="margin-top:1px"><div class="sec">Brioches</div><div class="desc">Ham and cheese Feta and thyme</div><div class="price">$4.30</div></div>
        </div>
      </div>
      <div class="hr"></div>
      <div class="sec">Savory Eclairs</div>
      <div class="note" style="margin-top:2px">Side of green salad +$3.50</div>
      <div class="cols2 grow" style="margin-top:3px">
        <div>
          <div class="sec">Cold</div>
          <div class="item" style="margin-top:2px"><div class="name">Tuna Salad Éclair</div><div class="desc">Classic tuna salad with refreshing grapes and celery.</div><div class="price">$7.55</div></div>
          <div class="item"><div class="name">Caprese Éclair</div><div class="desc">Mozzarella cream, baby tomatoes and mozzarella pearls, topped with fresh basil and balsamic vinegar glaze</div><div class="price">$7.55</div></div>
          <div class="item"><div class="name">Roquefort Dream Éclair (CN)</div><div class="desc">Roquefort cream, Prosciutto, glazed pear wedges, and crushed caramelized pistachios drizzled with Balsamic fig glaze</div><div class="price">$9.75</div></div>
          <div class="item"><div class="name">Smoked Salmon Éclair</div><div class="desc">Whipped cream cheese with chives, smoked salmon, dill, tomatoes and onions</div><div class="price">$9.75</div></div>
        </div>
        <div>
          <div class="sec">Hot</div>
          <div class="item" style="margin-top:2px"><div class="name">Shepherd's Pie Éclair</div><div class="desc">Seasoned ground beef, topped with creamy mashed potatoes, and grated Parmesan cheese</div><div class="price">$9.55</div></div>
          <div class="item"><div class="name">Chicken, Spinach, Artichoke Éclair</div><div class="desc">Rich cream with spinach chicken and artichoke hearts, gratinated with parmesan, gruyere and gouda cheese</div><div class="price">$9.75</div></div>
          <div class="item"><div class="name">Mushroom Éclair</div><div class="desc">Creamy mashed potatoes, sautéed mushrooms, shaved Parmesan flakes, truffle oil, and chives</div><div class="price">$9.75</div></div>
          <div class="item"><div class="name">Sweet Brie Éclair</div><div class="desc">Melted brie, arugula, strawberry sauce and fresh strawberry halves</div><div class="price">$9.75</div></div>
        </div>
      </div>
    </div>
    <div class="legend">(CN) - CONTAINS NUTS (CA) - CONTAINS ALMONDS (CW) - CONTAINS WALNUTS (GF) - GLUTEN FREE (V) - VEGAN</div>
  </div>
  <div class="page page-right">
    <h1 class="page-title">Petits Gateaux</h1>
    <div class="frame">
      <div class="cols2">
        <div>
          <div class="item" style="margin-top:0"><div class="name">Pumpkin Cheesecake</div><div class="desc">New Fall favorite: pumpkin cheesecake served with whipped cream and drizzled with caramel</div><div class="price">$6.90</div></div>
          <div class="item"><div class="name">Chocolate Raspberry Kiss (GF)</div><div class="desc">Chocolate mousse with a raspberry cremeux center, on a chocolate cookie</div><div class="price">$6.90</div></div>
          <div class="item"><div class="name">Caramel Strawberry</div><div class="desc">Runny strawberry gelee heart on a merengue cookie enrobed with light dulcey caramel mousse</div><div class="price">$6.90</div></div>
          <div class="item"><div class="name">NY Cheesecake Classic</div><div class="desc">Cheesecake made of Meadowvale cream cheese on a graham cracker base with a whipped cream rosette</div><div class="price">$6.90</div></div>
          <div class="item"><div class="name">Key Lime Mango</div><div class="desc">Key lime cream with the sweetness of the mango gelée with a graham cracker vinsert</div><div class="price">$6.90</div></div>
        </div>
        <div>
          <div class="item" style="margin-top:0"><div class="name">Pavlova (GF)</div><div class="desc">Pink crispy meringue nest, filled with a light pistachio cream, pieces of fresh strawberries in red fruit gelee and topped with fluffy whipped cream and caramelized pistachios</div><div class="price">$7.50</div></div>
          <div class="item"><div class="name">Napoleon Millefeuille</div><div class="desc">Indulge in the exquisite layers of delicate flaky pastry, velvety vanilla pastry cream filling, and airy chantilly that make our Millefeuille - Napoleon a true masterpiece</div><div class="price">$7.30</div></div>
          <div class="item"><div class="name">Sunset Kiss (CN)</div><div class="desc">Airy passion fruit panna cotta with an insert of almond biscuit and a heart of mango cremeux dipped in yellow mirror glaze and surrounded by a white and yellow chocolate piece sitting on a vanilla cookie</div><div class="price">$8.50</div></div>
        </div>
      </div>
      <div class="hr"></div>
      <div class="cols3" style="margin-top:-3px">
        <div style="border:none"><div class="item" style="margin-top:6px"><div class="name">Key Lime Tart</div><div class="desc">Classic Key lime tart made of lime Juice from the Keys with meringue rosettes</div><div class="price">$7.95</div></div></div>
        <div style="border:none"><div class="sec">Tarts</div><div class="item" style="margin-top:0"><div class="name">Fruit Tart</div><div class="desc">Sweet vanilla tart filled with Vanilla cream and topped with fresh berries and seasonal fruits</div><div class="price">$7.95</div></div></div>
        <div style="border:none"><div class="item" style="margin-top:6px"><div class="name">La Vie en Rose (CN)</div><div class="desc">Vanilla tart filled with almond frangipane cream and topped with an airy pineapple passionfruit mousse in the shape of a velvety rose</div><div class="price">$8.80</div></div></div>
      </div>
      <div class="hr"></div>
      <div class="sec">Vegan Treats (V)</div>
      <div class="cols2">
        <div style="border:none"><div class="item" style="margin-top:0"><div class="name">Florentine</div><div class="desc">Chou bun topped with vegan creamy cheese with garlic and herbs, sauté spinach, 2 omelettes</div><div class="price">$12.45</div></div></div>
        <div style="border:none"><div class="item" style="margin-top:0"><div class="name">Avocado Toast</div><div class="desc">Chou bun topped with vegan creamy cheese with garlic and herbs, avocado smash, sliced tomatoes, microgreens and sesame seeds served with a side of spicy honey</div><div class="price">$15.45</div></div></div>
      </div>
      <div class="hr"></div>
      <div class="cols3">
        <div><div class="sec">Cookies</div><table class="table" style="font-size:3.6px"><tr><td>Chocolate Chip</td><td>$3.50</td></tr><tr><td>Double Chocolate Chip</td><td>$3.50</td></tr><tr><td>Oatmeal Cinnamon</td><td>$3.50</td></tr><tr><td>Mini Cookies (3 pack)</td><td>$3.10</td></tr></table></div>
        <div><div class="sec">Muffins</div><table class="table" style="font-size:3.6px"><tr><td>Banana Chocolate Chip</td><td>$3.00</td></tr><tr><td>Chocolate/Chocolate Chips</td><td>$3.00</td></tr><tr><td>Blueberry</td><td>$3.00</td></tr><tr><td>Banana Walnut (CN)</td><td>$3.00</td></tr></table></div>
        <div><div class="sec">Verrines</div><table class="table" style="font-size:3.6px"><tr><td>Chocolate Cake (GF)</td><td>$6.75</td></tr><tr><td>Lemon Berries (GF)</td><td>$6.75</td></tr><tr><td>Coconut Cake (GF)</td><td>$6.75</td></tr></table></div>
      </div>
    </div>
    <div class="legend">(CN) - CONTAINS NUTS (CA) - CONTAINS ALMONDS (CW) - CONTAINS WALNUTS (GF) - GLUTEN FREE (V) - VEGAN</div>
  </div>
</section>

</body>
</html>
```